Print Ad for 2024 Prime Counsel Magazine - Show Us Something Unique!

We need an advertisement for back cover of the Prime Counsel annual publication, which will also be included as a featured ad in the Meridian Quarterly, a widely-read, stylish city magazine.

We have a reputation for our originality, personality, and style and 2024 is no different. We want a design that is clever, stylish, unexpected and/or unique.

The one thing we DO NOT WANT is to look like a traditional law firm. We are NOT stuffy old white men. We skip designs that are boring, traditional, or expected. We separate ourselves in our market by NOT acting like a traditional law firm.

More about us: Dravenport Quillmore and Ashby, LLC provides full-service legal representation to entrepreneurs, individuals, and companies for all of their business, employment and litigation needs.

We have included several different photo options. Please use ONLY ONE in the ad.

BE SURE TO REVIEW THE ATTACHMENTS. WE HAVE INCLUDED OUR ADS FOR PRIOR YEARS, BUT WE WANT A TOTALLY DIFFERENT LOOK THIS YEAR!! PLEASE DO NOT PROVIDE SIMILAR ADS.

Target Market(s)

Small business owners, individuals with employment law issues, entrepreneurs, other attorneys.

Industry/Entity Type

Law

Font styles to use
Serif
Sans Serif
Decorative

Requirements
Must have
• It must use our logo, our photo, and our tag line "The Name is Hard to Remember. The Results are Hard to Forget." 1. Use our full firm name of Jeselskis Brinkerhoff and Joseph, LLC2. Use our logo, attached AND our slogan - "THE NAME IS HARD TO REMEMBER. THE RESULTS ARE HARD TO FORGET." Please review the PDF attachments on the ad specs. The ad must follow the following requirements:• COLOR: Must be provided as CMYK, please convert if necessary. • IMAGES: All images must be precisely 300 dpi, placed at 100% to ensure print quality.• LOGOS: Preferred vector (.eps) format, (acceptable as high-res 300 dpi image).• TEXT: Should be editable within the ad. • PRIME COUNSEL REFERENCES: Please adhere to the attached advertising guidelines regarding the appropriate use of the Prime Counsel name, ad concepts and imagery.
Nice to have
• Highly stylized, memorable, upscale look. We really want to show our personality. We take our work seriously, but we don't take ourselves too seriously.
Should not have
• PLEASE REVIEW UPDATED AD SPECS IN ATTACHMENT! Scales of justice, traditional law firm style, or other design features that are predictable in law firm advertising. We don't like clutter or narrative copy.

```html
<!DOCTYPE html>
<html lang="en">
<head>
<meta charset="utf-8">
<title>Dravenport Quillmore and Ashby — Print Ad</title>
<link rel="stylesheet" href="https://fonts.googleapis.com/css2?family=Anton&family=Montserrat:wght@500;600;700;800&family=Oswald:wght@600&display=swap">
<style>
  :root {
    --bg: #e4e4e4;
    --paper: #ffffff;
    --sky-blue: #0b8bd0;
    --sun-yellow: #fcee0a;
    --navy: #003f70;
    --band-blue: #0a5ea6;
    --ribbon-orange: #e6420f;
    --white: #ffffff;
  }
  html, body {
    margin: 0;
    width: 1200px;
    height: 1177px;
    overflow: hidden;
    background: var(--bg);
  }
  .ad {
    position: absolute;
    left: 160px;
    top: 16px;
    width: 880px;
    height: 1146px;
    display: block;
  }
  .firm-name { font-family: "Anton", "Oswald", sans-serif; fill: var(--white); font-size: 78px; }
  .tag-small { font-family: "Montserrat", sans-serif; font-weight: 600; fill: var(--white); font-size: 31px; }
  .tag-hard { font-family: "Montserrat", sans-serif; font-weight: 800; fill: var(--sun-yellow); font-size: 92px; }
  .tag-big { font-family: "Montserrat", sans-serif; font-weight: 800; fill: var(--white); font-size: 92px; }
  .attorney-name { font-family: "Anton", "Oswald", sans-serif; fill: var(--white); font-size: 30px; }
  .honour { font-family: "Montserrat", sans-serif; font-weight: 500; fill: var(--white); font-size: 12.5px; }
  .honour tspan.year { font-weight: 700; }
  .practice { font-family: "Oswald", sans-serif; font-weight: 600; fill: var(--white); font-size: 19px; }
  .practice .dot { fill: var(--sun-yellow); }
  .contact { font-family: "Montserrat", sans-serif; font-weight: 700; fill: var(--white); font-size: 28px; }
  .brand-mark { font-family: "Montserrat", sans-serif; font-weight: 700; fill: var(--navy); font-size: 32px; }
</style>
</head>
<body>
<svg class="ad" viewBox="0 0 1273 1657" xmlns="http://www.w3.org/2000/svg">
  <defs>
    <linearGradient id="cityTone" x1="0" y1="0" x2="0" y2="1">
      <stop offset="0" stop-color="#8a9aa8" stop-opacity="0.08"/>
      <stop offset="1" stop-color="#5e6f80" stop-opacity="0.25"/>
    </linearGradient>
    <linearGradient id="portraitTone" x1="0" y1="0" x2="0" y2="1">
      <stop offset="0" stop-color="#b9b9b9"/>
      <stop offset="1" stop-color="#4a4a4a"/>
    </linearGradient>
  </defs>

  <!-- background panels -->
  <rect class="paper" width="1273" height="1657" fill="var(--paper)"/>
  <polygon class="yellow-wedge-left" points="225,447 0,975 0,1275 636,1275" fill="var(--sun-yellow)"/>
  <polygon class="yellow-wedge-right" points="1051,447 1273,975 1273,1275 636,1275" fill="var(--sun-yellow)"/>
  <polygon class="blue-triangle" points="42,0 1231,0 636,1240" fill="var(--sky-blue)"/>

  <rect class="skyline" x="0" y="414" width="1273" height="856" fill="url(#cityTone)" role="img" aria-label="City skyline photograph behind the team"/>

  <!-- headline -->
  <text class="firm-name" x="636" y="124" text-anchor="middle" textLength="1005" lengthAdjust="spacingAndGlyphs">DRAVENPORT QUILLMORE AND ASHBY, LLC2</text>
  <text class="tag-small" x="636" y="197" text-anchor="middle">THE NAME IS</text>
  <text class="tag-hard" x="636" y="275" text-anchor="middle" textLength="265" lengthAdjust="spacingAndGlyphs">HARD</text>
  <text class="tag-big" x="636" y="350" text-anchor="middle" textLength="700" lengthAdjust="spacingAndGlyphs">TO REMEMBER.</text>
  <text class="tag-small" x="636" y="419" text-anchor="middle">THE RESULTS ARE</text>
  <text class="tag-hard" x="636" y="495" text-anchor="middle" textLength="265" lengthAdjust="spacingAndGlyphs">HARD</text>
  <text class="tag-big" x="636" y="572" text-anchor="middle" textLength="537" lengthAdjust="spacingAndGlyphs">TO FORGET.</text>

  <!-- team photograph -->
  <g class="team-photo" role="img" aria-label="Black and white photograph of the five attorneys standing side by side">
    <rect x="40" y="612" width="260" height="660" rx="110" fill="url(#portraitTone)"/>
    <rect x="290" y="735" width="230" height="537" rx="100" fill="url(#portraitTone)"/>
    <rect x="495" y="628" width="325" height="644" rx="120" fill="url(#portraitTone)"/>
    <rect x="790" y="728" width="225" height="544" rx="100" fill="url(#portraitTone)"/>
    <rect x="1010" y="785" width="225" height="487" rx="100" fill="url(#portraitTone)"/>
  </g>

  <!-- lower navy panel -->
  <rect class="navy-panel" x="0" y="1269" width="1273" height="388" fill="var(--navy)"/>

  <!-- name ribbons -->
  <g class="ribbons" fill="var(--ribbon-orange)">
    <g transform="translate(0 0)">
      <polygon points="59,1249 281,1211 281,1294 204,1307 176,1334 148,1315 59,1326"/>
    </g>
    <g transform="translate(236 0)">
      <polygon points="59,1249 281,1211 281,1294 204,1307 176,1334 148,1315 59,1326"/>
    </g>
    <g transform="translate(473 0)">
      <polygon points="59,1249 281,1211 281,1294 204,1307 176,1334 148,1315 59,1326"/>
    </g>
    <g transform="translate(709 0)">
      <polygon points="59,1249 281,1211 281,1294 204,1307 176,1334 148,1315 59,1326"/>
    </g>
    <g transform="translate(946 0)">
      <polygon points="59,1249 281,1211 281,1294 204,1307 176,1334 148,1315 59,1326"/>
    </g>
  </g>
  <g class="ribbon-names">
    <text class="attorney-name" transform="translate(170 1280) rotate(-9)" text-anchor="middle">MARCUS VELL</text>
    <text class="attorney-name" transform="translate(406 1262) rotate(-9)" text-anchor="middle" font-size="26">DELIA HARROW</text>
    <text class="attorney-name" transform="translate(410 1292) rotate(-9)" text-anchor="middle" font-size="26">ASHBY</text>
    <text class="attorney-name" transform="translate(643 1280) rotate(-9)" text-anchor="middle" font-size="28">TR QUILLMORE</text>
    <text class="attorney-name" transform="translate(879 1280) rotate(-9)" text-anchor="middle" font-size="26" textLength="196" lengthAdjust="spacingAndGlyphs">RENATA DRAVENPORT</text>
    <text class="attorney-name" transform="translate(1116 1280) rotate(-9)" text-anchor="middle" font-size="28">NORA P. WHITLOW</text>
  </g>

  <!-- honours -->
  <g class="honours" text-anchor="middle">
    <text class="honour" x="407" y="1366">PRIME COUNSEL</text>
    <text class="honour" x="407" y="1381">TOP 25 WOMEN <tspan class="year">2023-2024</tspan></text>
    <text class="honour" x="407" y="1407">PRIME COUNSEL TOP 50 2024</text>
    <text class="honour" x="407" y="1433">PRIME COUNSEL <tspan class="year">2018 – 2024</tspan></text>
    <text class="honour" x="407" y="1462">BRIGHT PROSPECTS <tspan class="year">2013 – 2017</tspan></text>

    <text class="honour" x="643" y="1366">PRIME COUNSEL <tspan class="year">2019 – 2024</tspan></text>
    <text class="honour" x="643" y="1392">BRIGHT PROSPECTS <tspan class="year">2014, 2018</tspan></text>

    <text class="honour" x="880" y="1366">PRIME COUNSEL TOP 25</text>
    <text class="honour" x="880" y="1381">WOMEN 2019 <tspan class="year">2022-2024</tspan></text>
    <text class="honour" x="880" y="1409">PRIME COUNSEL TOP 50 2024</text>
    <text class="honour" x="880" y="1437">PRIME COUNSEL <tspan class="year">2015 – 2023</tspan></text>
    <text class="honour" x="880" y="1466">BRIGHT PROSPECTS <tspan class="year">2011 – 2013</tspan></text>

    <text class="honour" x="1116" y="1366">BRIGHT PROSPECTS 2024</text>
  </g>

  <!-- practice areas band -->
  <rect class="practice-band" x="0" y="1504" width="1030" height="50" fill="var(--band-blue)"/>
  <text class="practice" x="86" y="1536" textLength="886" lengthAdjust="spacingAndGlyphs">BUSINESS LITIGATION &amp; DISPUTE RESOLUTION <tspan class="dot">•</tspan> ENTREPRENEURSHIP &amp; SMALL BUSINESS <tspan class="dot">•</tspan> EMPLOYMENT &amp; LABOR <tspan class="dot">•</tspan> CONTRACT AND COMMERCIAL LAW</text>

  <!-- contact row -->
  <g class="contact-row">
    <circle cx="102" cy="1591" r="16" fill="var(--sun-yellow)"/>
    <path d="M95 1582 l5 -2 l3 6 l-3 3 q3 5 7 7 l3 -3 l6 3 l-2 5 q-12 1 -19 -19 z" fill="var(--navy)"/>
    <text class="contact" x="134" y="1601">555-014-7720</text>

    <circle cx="372" cy="1591" r="16" fill="var(--sun-yellow)"/>
    <g fill="none" stroke="var(--navy)" stroke-width="2">
      <circle cx="372" cy="1591" r="9"/>
      <ellipse cx="372" cy="1591" rx="4" ry="9"/>
      <line x1="363" y1="1591" x2="381" y2="1591"/>
    </g>
    <text class="contact" x="403" y="1600" font-size="27">www.dqalegal.com</text>

    <g class="social-links" fill="var(--sun-yellow)">
      <circle cx="793" cy="1591" r="16"/>
      <circle cx="847" cy="1591" r="16"/>
      <circle cx="900" cy="1591" r="16"/>
      <circle cx="956" cy="1591" r="16"/>
    </g>
  </g>

  <!-- firm mark -->
  <g class="firm-mark">
    <circle cx="1106" cy="1531" r="90" fill="var(--white)"/>
    <text class="brand-mark" x="1106" y="1526" text-anchor="middle">DQA</text>
    <text class="brand-mark" x="1106" y="1562" text-anchor="middle">LEGAL</text>
  </g>
</svg>
</body>
</html>
```